KP7 Medical Needs a Catalogue Design

KP7 Medical is in need of a serious, professional catalogue design to outline our company profile, certifications and showcase our products. Profile, contact details and product information is available via our website www.kp7medical.example . Non watermarked photos, company certificates, factory photos etc will be made available upon successful designer selection.

Target Market(s)

Existing and potential customers. Initially in Malaysia, Asia, Europe

Industry/Entity Type

Healthcare

Requirements
Must have
• Company Logo
• KP7 Medical 'red' colour which is available as shown on logo
• A world map with arrows from Malaysia across the world showing exporting
• Velbrook Certa ISO 13485:2012 Quality Assurance Logo
• Quality Hi res Medical/Healthcare photos
• Social Medical links (Chatterly, Pipster, Loopnet+)
• Wayfind Map showing location

```html
<!DOCTYPE html>
<html lang="en">
<head>
<meta charset="utf-8">
<title>KP7 Medical Catalogue – Spread 1–2</title>
<link rel="stylesheet" href="https://fonts.googleapis.com/css2?family=Roboto:ital,wght@0,400;0,500;0,700;0,900;1,700&display=swap">
<style>
  :root {
    --brand: #ad0f55;
    --brand-dark: #8a0b43;
    --ink: #2b2b2b;
    --muted: #6d6d6d;
    --stripe: #1e1c1d;
    --paper: #ffffff;
    --backdrop: #e6e3df;
    --photo-a: #c9d6e3;
    --photo-b: #8fa9c4;
  }
  * { box-sizing: border-box; margin: 0; padding: 0; }
  html, body { width: 1200px; height: 900px; overflow: hidden; }
  body {
    background: var(--backdrop);
    font-family: "Roboto", Arial, sans-serif;
    color: var(--ink);
    position: relative;
  }
  .spread {
    position: absolute; left: 30px; top: 60px;
    width: 1140px; height: 780px;
    background: var(--paper);
    box-shadow: 0 10px 30px rgba(0,0,0,.18);
    overflow: hidden;
  }
  .spread-art { position: absolute; inset: 0; }
  .fold {
    position: absolute; left: 560px; top: 0; width: 20px; height: 780px;
    background: linear-gradient(90deg, rgba(0,0,0,0) 0%, rgba(0,0,0,.18) 50%, rgba(0,0,0,0) 100%);
  }

  .tag {
    position: absolute;
    background: var(--brand);
    color: #fff;
    font-weight: 900;
    font-size: 12px;
    letter-spacing: .3px;
    text-transform: uppercase;
    white-space: nowrap;
    padding: 4px 22px 4px 10px;
    clip-path: polygon(0 0, calc(100% - 12px) 0, 100% 50%, calc(100% - 12px) 100%, 0 100%);
  }
  .tag--lower { text-transform: none; font-size: 11px; font-weight: 700; }

  /* left page */
  .about {
    position: absolute; left: 40px; top: 56px; width: 505px;
    font-size: 10.3px; line-height: 1.32; color: var(--muted);
  }
  .about p + p { margin-top: 6px; }
  .about .lead { font-weight: 700; color: #7b7b7b; }
  .about .accent { font-weight: 700; color: var(--brand); }

  .strengths {
    position: absolute; left: 40px; top: 318px; width: 320px;
    list-style: none; font-size: 10.5px; line-height: 1.4; color: var(--ink);
  }
  .strengths li { padding-left: 16px; position: relative; }
  .strengths li::before {
    content: ""; position: absolute; left: 2px; top: 4px;
    width: 6px; height: 6px;
    border-top: 2px solid var(--brand); border-right: 2px solid var(--brand);
    transform: rotate(45deg);
  }

  .index {
    position: absolute; left: 118px; top: 418px; width: 240px;
    border-collapse: collapse; font-size: 10.5px; color: var(--brand); font-weight: 700;
  }
  .index th, .index td { border: 1px solid var(--brand); padding: 2px 6px; text-align: left; white-space: nowrap; }
  .index td.page { width: 48px; color: var(--ink); font-weight: 500; }

  .cert-badge {
    position: absolute; left: 40px; top: 680px; width: 90px; height: 54px;
    background: #eef0f3; border: 1px solid #c9ced6;
  }
  .cert-badge::before {
    content: ""; position: absolute; left: 6px; top: 6px; width: 40px; height: 40px;
    background: #2f5fa8;
  }
  .export-map {
    position: absolute; left: 150px; top: 678px; width: 110px; height: 58px;
    background: linear-gradient(135deg, #dbe7f2, #b8cde2);
  }
  .page-no {
    position: absolute; bottom: 26px; width: 34px; height: 18px;
    background: var(--brand); color: #fff; font-weight: 700; font-size: 11px;
    line-height: 18px; text-align: center;
  }
  .page-no--left { left: 0; clip-path: polygon(0 0, 100% 0, 80% 100%, 0 100%); }
  .page-no--right { right: 0; clip-path: polygon(20% 0, 100% 0, 100% 100%, 0 100%); }

  /* right page product blocks */
  .spec {
    position: absolute; border-collapse: collapse; background: #fff;
    font-size: 10px; color: var(--ink);
    border: 1.5px solid var(--stripe);
  }
  .spec th, .spec td {
    border: 1px solid #555; padding: 3px 6px; vertical-align: top; text-align: left;
    white-space: nowrap;
  }
  .spec th { width: 92px; font-weight: 700; background: #f4f4f4; }
  .spec--30 { left: 650px; top: 200px; }
  .spec--60 { left: 596px; top: 440px; }
  .swatch {
    display: inline-block; background: var(--brand); color: #fff;
    padding: 0 5px; margin: 0 8px;
  }
  .spec ul { list-style: none; }
  .spec li { padding-left: 14px; position: relative; line-height: 1.35; }
  .spec li::before {
    content: ""; position: absolute; left: 1px; top: 3px;
    width: 7px; height: 7px; border: 1px solid #555; border-radius: 50%;
  }

  .order {
    position: absolute; border-collapse: collapse; background: #fff;
    font-size: 9.5px; color: var(--ink); border: 1px solid var(--brand);
  }
  .order th { color: var(--brand); font-weight: 700; text-align: left; }
  .order th, .order td { border: 1px solid var(--brand); padding: 1px 4px; white-space: nowrap; }
  .order td:first-child { font-weight: 700; }
  .order--30 { left: 988px; top: 272px; }
  .order--60 { left: 930px; top: 582px; }

  .product-photo { position: absolute; }
</style>
</head>
<body>
<main class="spread">
  <svg class="spread-art" width="1140" height="780" viewBox="0 0 1140 780" aria-hidden="true">
    <polygon points="548,170 570,170 570,780 262,780 505,400" fill="var(--brand)"/>
    <polygon points="530,420 556,420 252,780 226,780" fill="var(--stripe)"/>
    <polygon points="570,0 748,0 712,228 700,350 650,400 720,470 790,470 830,780 570,780" fill="var(--brand)"/>
    <polygon points="705,230 728,230 712,350 690,350" fill="var(--stripe)"/>
    <polygon points="760,385 790,385 748,440 790,470 762,470 720,440" fill="var(--stripe)"/>
    <polygon points="840,660 864,660 905,780 881,780" fill="var(--stripe)"/>
  </svg>
  <div class="fold" aria-hidden="true"></div>

  <!-- ===== Page 1 ===== -->
  <section class="page page--left">
    <h2 class="tag" style="left:34px; top:26px;">About Us</h2>
    <div class="about">
      <p class="lead">We pride ourselves in our ‘can-do’ attitude and adopt a proactive approach in all areas of our medical products manufacturing.</p>
      <p>We are committed to offering quality competitively priced interchangeable polymer alternatives to stainless steel products. In most cases, our products are similarly autoclavable, washable and reusable, or can be used as a purely disposable or single patient item. <span class="accent">Not only can our products offer the same usability and flexibility to our customers</span>, but at a lower outlay cost.</p>
      <p>Our products have been designed to offer solutions to a variety of patient, staff and environmental problems that challenge the healthcare industry particularly in regards to safety and infection control. In addition to this, we are proud to have a ‘can do’ attitude and adopt a proactive approach when developing new products. Through consultation with key stakeholders during the design phase of new product development, we ensure that new KP7 Medical products successfully meet all of the needs of our customers from an early stage. To keep up with changes in technology and workplace practices, KP7 Medical continues to modify and adapt its products to ensure that our customers are getting the best products available.</p>
    </div>

    <h3 class="tag tag--lower" style="left:34px; top:292px;">Key strengths include:</h3>
    <ul class="strengths">
      <li>Experienced medical products manufacturer.</li>
      <li>Committed to the highest level of quality.</li>
      <li>Provide exceptional customer service.</li>
      <li>Flexibility to meet your needs.</li>
      <li>We get to know our customers.</li>
      <li>Your success is our success.</li>
    </ul>

    <table class="index">
      <tr><th colspan="2">INDEX</th></tr>
      <tr><td>Medicine Dispensing Cups</td><td class="page">2</td></tr>
      <tr><td>Disposable Bowls</td><td class="page">3-5</td></tr>
      <tr><td>Autoclavable Bowls</td><td class="page">6-9</td></tr>
      <tr><td>Kidney Dishes</td><td class="page">10-12</td></tr>
      <tr><td>Injection/Procedure Trays</td><td class="page">13-14</td></tr>
      <tr><td>Gallipots</td><td class="page">15-16</td></tr>
      <tr><td>Denture / Multi Purpose Bowls &amp; Lids</td><td class="page">17</td></tr>
      <tr><td>Notes</td><td class="page">18</td></tr>
    </table>

    <div class="cert-badge" role="img" aria-label="Velbrook Certa ISO 13485 certification badge"></div>
    <div class="export-map" role="img" aria-label="World map with export arrows from Malaysia"></div>

    <svg class="product-photo" style="left:392px; top:352px;" width="176" height="156" viewBox="0 0 176 156" role="img" aria-label="Photo of a smiling team of doctors and nurses">
      <defs>
        <linearGradient id="photoTeam" x1="0" y1="0" x2="1" y2="1">
          <stop offset="0" stop-color="var(--photo-a)"/><stop offset="1" stop-color="var(--photo-b)"/>
        </linearGradient>
      </defs>
      <polygon points="44,4 132,4 172,78 132,152 44,152 4,78" fill="url(#photoTeam)" stroke="var(--stripe)" stroke-width="7"/>
    </svg>
    <div class="page-no page-no--left">1</div>
  </section>

  <!-- ===== Page 2 ===== -->
  <section class="page page--right">
    <svg class="product-photo" style="left:545px; top:32px;" width="180" height="160" viewBox="0 0 180 160" role="img" aria-label="Photo of hospital staff in white coats and scrubs">
      <defs>
        <linearGradient id="photoStaff" x1="0" y1="0" x2="1" y2="1">
          <stop offset="0" stop-color="#e4e8ee"/><stop offset="1" stop-color="#9fb4cc"/>
        </linearGradient>
      </defs>
      <polygon points="46,4 134,4 176,80 134,156 46,156 4,80" fill="url(#photoStaff)" stroke="var(--stripe)" stroke-width="7"/>
    </svg>

    <h2 class="tag" style="left:660px; top:172px;">30ml Medicine Dispensing Cups</h2>
    <table class="spec spec--30">
      <tr><th>Quantity Options</th><td>5000 pieces/carton; (50 sleeves x 100 pieces)<br>500 pieces; (5 sleeves x 100 pieces)<br>100 pieces; (1 sleeve x 100 pieces)</td></tr>
      <tr><th>Capacity</th><td>30mL</td></tr>
      <tr><th>Graduations</th><td>2.5, 5, 7.5, 10, 15, 20, 25, 30mL</td></tr>
      <tr><th>Colours</th><td>Clear<span class="swatch">Opaque Red</span>Other upon request</td></tr>
      <tr><th>Material</th><td>Polypropylene</td></tr>
      <tr><th>Other</th><td><ul><li>Non Sterile</li><li>Single Patient Use symbol on base</li><li>Recyclable PP symbol on base</li><li>Latex Free</li></ul></td></tr>
    </table>
    <svg class="product-photo" style="left:990px; top:108px;" width="150" height="160" viewBox="0 0 150 160" role="img" aria-label="Product shots of red and clear 30ml dispensing cups">
      <polygon points="18,2 58,2 76,38 58,74 18,74 0,38" fill="#2a2a2a"/>
      <polygon points="24,11 52,11 66,38 52,65 24,65 10,38" fill="#d98a8e"/>
      <polygon points="70,80 110,80 128,116 110,152 70,152 52,116" fill="#2a2a2a"/>
      <polygon points="76,89 104,89 118,116 104,143 76,143 62,116" fill="#e7e5e0"/>
    </svg>
    <table class="order order--30">
      <tr><th>Order Code</th><th>Quantity</th><th>Colour</th></tr>
      <tr><td>MM30</td><td>5000</td><td>Clear</td></tr>
      <tr><td>MM30R</td><td>5000</td><td>Red</td></tr>
      <tr><td>MM30-500</td><td>500</td><td>Clear</td></tr>
      <tr><td>MM30R-500</td><td>500</td><td>Red</td></tr>
      <tr><td>MM30-100</td><td>100</td><td>Clear</td></tr>
      <tr><td>MM30R-100</td><td>100</td><td>Red</td></tr>
    </table>

    <h2 class="tag" style="left:600px; top:412px;">60ml Medicine Dispensing Cups</h2>
    <table class="spec spec--60">
      <tr><th>Quantity Options</th><td>1000 pieces/carton; (40 sleeves x 25 pieces)<br>500 pieces; (20 sleeves x 25 pieces)<br>25 pieces; (1 sleeve x 25 pieces)</td></tr>
      <tr><th>Capacity</th><td>60mL</td></tr>
      <tr><th>Graduations</th><td>5, 10, 15, 20, 25, 30, 35, 40, 45, 50, 55, 60mL</td></tr>
      <tr><th>Colours</th><td>Clear<span class="swatch">Opaque Red</span>Other upon request</td></tr>
      <tr><th>Material</th><td>Polypropylene</td></tr>
      <tr><th>Other</th><td><ul><li>Non Sterile</li><li>Single Patient Use symbol on base</li><li>Recyclable PP symbol on base</li><li>Latex Free</li></ul></td></tr>
    </table>
    <svg class="product-photo" style="left:950px; top:418px;" width="160" height="156" viewBox="0 0 160 156" role="img" aria-label="Product shots of clear and red 60ml dispensing cups">
      <polygon points="18,2 58,2 76,38 58,74 18,74 0,38" fill="#2a2a2a"/>
      <polygon points="24,11 52,11 66,38 52,65 24,65 10,38" fill="#e9e8e4"/>
      <polygon points="80,78 120,78 138,114 120,150 80,150 62,114" fill="#2a2a2a"/>
      <polygon points="86,87 114,87 128,114 114,141 86,141 72,114" fill="#d98a8e"/>
    </svg>
    <table class="order order--60">
      <tr><th>Order Code</th><th>Quantity</th><th>Colour</th></tr>
      <tr><td>MM60</td><td>1000</td><td>Clear</td></tr>
      <tr><td>MM60R</td><td>1000</td><td>Red</td></tr>
      <tr><td>MM60-500</td><td>500</td><td>Clear</td></tr>
      <tr><td>MM60R-500</td><td>500</td><td>Red</td></tr>
      <tr><td>MM60-25</td><td>25</td><td>Clear</td></tr>
      <tr><td>MM60R-25</td><td>25</td><td>Red</td></tr>
    </table>
    <div class="page-no page-no--right">2</div>
  </section>
</main>
</body>
</html>
```